Glint5Gate Photography Business Cards

We need a good general business card that we can hand to our clients. We will be doing embossed gloss cards.

Target Market(s)

Real estate / Business to business / professionals

```html
<!DOCTYPE html>
<html lang="en">
<head>
<meta charset="utf-8">
<title>Glint5Gate Photography – Business Cards</title>
<link href="https://fonts.googleapis.com/css2?family=Poppins:wght@300;400;600&display=swap" rel="stylesheet">
<style>
  :root {
    --backdrop: #2b2d32;
    --card: #272468;
    --card-edge: #1c1a52;
    --ink-white: #ffffff;
    --ink-soft: #d9dbef;
    --accent: #2fa6e3;
    --silver: #c9ccd6;
    --emboss: rgba(255,255,255,0.07);
  }
  * { box-sizing: border-box; margin: 0; padding: 0; }
  html, body {
    width: 1200px; height: 900px; overflow: hidden;
    background: var(--backdrop);
    font-family: "Poppins", sans-serif;
  }
  .stage {
    position: relative; width: 1200px; height: 900px;
    display: flex; flex-direction: column; align-items: center; justify-content: center; gap: 44px;
  }
  .card {
    position: relative; width: 660px; height: 377px;
    background: var(--card);
    box-shadow: 0 4px 0 var(--card-edge), 0 14px 30px rgba(0,0,0,0.45);
    overflow: hidden;
  }
  /* front */
  .brand {
    position: absolute; left: 52px; top: 50px;
    display: flex; align-items: center; gap: 12px;
  }
  .brand-dot {
    width: 14px; height: 14px; border-radius: 50%; background: var(--accent);
  }
  .brand-name {
    font-weight: 600; font-size: 30px; color: var(--ink-white); letter-spacing: 0.5px;
  }
  .person {
    position: absolute; left: 52px; top: 190px;
  }
  .person-name { font-size: 22px; font-weight: 400; color: var(--ink-white); }
  .person-role { font-size: 14px; font-weight: 300; color: var(--accent); margin-top: 2px; }
  .divider {
    position: absolute; left: 270px; top: 180px; width: 1px; height: 118px;
    background: rgba(255,255,255,0.35);
  }
  .contacts {
    position: absolute; left: 290px; top: 184px; list-style: none;
    display: flex; flex-direction: column; gap: 12px;
  }
  .contacts li {
    display: flex; align-items: center; gap: 10px;
    font-size: 15px; font-weight: 300; color: var(--ink-soft);
  }
  .contacts svg { width: 15px; height: 15px; flex: none; }
  .emboss-seal {
    position: absolute; right: 40px; bottom: -30px; width: 230px; height: 230px;
    border-radius: 50%; border: 3px solid var(--emboss);
    box-shadow: inset 0 0 0 26px rgba(255,255,255,0.02);
  }
  /* back */
  .card--back .brand {
    left: 0; right: 0; top: 0; bottom: 0; justify-content: center;
  }
  .card--back .brand-name { color: var(--silver); font-size: 34px; }
  .card--back .brand-dot { background: var(--silver); width: 16px; height: 16px; }
</style>
</head>
<body>
<main class="stage">
  <section class="card card--front" aria-label="Card front">
    <div class="brand">
      <span class="brand-dot"></span>
      <span class="brand-name">Glint5Gate Photography</span>
    </div>
    <div class="person">
      <p class="person-name">Marcus Ellery</p>
      <p class="person-role">Photographer</p>
    </div>
    <div class="divider"></div>
    <ul class="contacts">
      <li>
        <svg viewBox="0 0 16 16" aria-hidden="true"><circle cx="8" cy="8" r="8" fill="var(--accent)"/><path d="M5.2 4.2l1.4-.2.8 2-1 .8c.5 1.1 1.3 1.9 2.4 2.4l.8-1 2 .8-.2 1.4c-3.4.3-6.5-2.8-6.2-6.2z" fill="var(--card)"/></svg>
        360.555.0142
      </li>
      <li>
        <svg viewBox="0 0 16 16" aria-hidden="true"><rect x="1" y="3" width="14" height="10" rx="1.5" fill="var(--accent)"/><path d="M1.5 4l6.5 5 6.5-5" stroke="var(--card)" stroke-width="1.3" fill="none"/></svg>
        info@glint5gatephotography.com
      </li>
      <li>
        <svg viewBox="0 0 16 16" aria-hidden="true"><circle cx="8" cy="8" r="7" fill="none" stroke="var(--accent)" stroke-width="1.4"/><ellipse cx="8" cy="8" rx="3" ry="7" fill="none" stroke="var(--accent)" stroke-width="1.2"/><path d="M1 8h14" stroke="var(--accent)" stroke-width="1.2"/></svg>
        www.glint5gatephotography.com
      </li>
    </ul>
    <div class="emboss-seal" aria-hidden="true"></div>
  </section>

  <section class="card card--back" aria-label="Card back">
    <div class="brand">
      <span class="brand-dot"></span>
      <span class="brand-name">Glint5Gate Photography</span>
    </div>
  </section>
</main>
</body>
</html>
```